Modern Business Card

Modern professional business card with more than just logo and demographic info. Something memorable.

We are a trendy/modern chiropractic group with an emphasis on neurology, hence the minimalist-type brain logo. We want to convey that modern and technical aspect with professionalism and the elite nature of our practice environment.

```html
<!DOCTYPE html>
<html lang="en">
<head>
<meta charset="utf-8">
<title>Keystone Spine – Business Card</title>
<link rel="stylesheet" href="https://fonts.googleapis.com/css2?family=Lato:wght@400;700&display=swap">
<style>
  :root {
    --page: #ffffff;
    --card-front: #fdfdfd;
    --brand-blue: #4a80c4;
    --brand-tint: #e9edf6;
    --map-shade: rgba(38, 86, 156, 0.38);
    --ink: #1c1c1c;
    --muted: #6f6f6f;
    --paper-white: #ffffff;
  }
  * { margin: 0; padding: 0; box-sizing: border-box; }
  html, body {
    width: 1200px; height: 1200px; overflow: hidden;
    background: var(--page);
    font-family: "Lato", Arial, sans-serif;
  }
  .canvas { position: relative; width: 1200px; height: 1200px; }

  .card { position: absolute; overflow: hidden; }
  .card--front {
    left: 232px; top: 173px; width: 705px; height: 407px;
    background: var(--card-front);
    box-shadow: 0 0 0 1px #ececec;
  }
  .card--back {
    left: 231px; top: 629px; width: 702px; height: 400px;
    background: var(--brand-blue);
  }

  /* faint brand pattern zone on the front, right half */
  .pattern-zone {
    position: absolute; left: 332px; top: 0; width: 373px; height: 407px;
    background:
      radial-gradient(ellipse 60% 55% at 55% 50%, var(--brand-tint) 0%, rgba(233, 237, 246, 0.75) 55%, rgba(233, 237, 246, 0) 100%);
  }

  .wordmark { position: absolute; display: flex; align-items: center; }
  .wordmark__square { background: var(--brand-blue); flex: none; }
  .wordmark__name {
    font-weight: 700; text-transform: uppercase; line-height: 1;
    display: flex; flex-direction: column;
  }
  .card--front .wordmark { left: 43px; top: 56px; gap: 14px; }
  .card--front .wordmark__square { width: 30px; height: 30px; }
  .card--front .wordmark__name { color: var(--ink); font-size: 34px; letter-spacing: 1px; gap: 4px; }

  .holder { position: absolute; right: 43px; top: 60px; text-align: right; }
  .holder__name { color: var(--brand-blue); font-size: 32px; font-weight: 700; line-height: 1.05; }
  .holder__role { color: var(--muted); font-size: 21px; margin-top: 4px; }

  .contact-list { position: absolute; left: 42px; top: 259px; list-style: none; }
  .contact-list li {
    display: flex; align-items: center; gap: 9px;
    color: var(--muted); font-size: 19px; height: 27px;
  }
  .contact-list svg { width: 20px; height: 20px; fill: var(--brand-blue); flex: none; }

  .address { position: absolute; right: 43px; top: 288px; text-align: right; color: var(--muted); font-size: 19px; line-height: 24px; }
  .address svg { width: 18px; height: 26px; fill: var(--brand-blue); display: block; margin: 0 0 6px auto; }

  .world-map {
    position: absolute; left: 10px; top: 15px; width: 690px; height: 370px;
    background:
      radial-gradient(ellipse 22% 30% at 22% 30%, var(--map-shade), rgba(38, 86, 156, 0) 100%),
      radial-gradient(ellipse 14% 30% at 30% 75%, var(--map-shade), rgba(38, 86, 156, 0) 100%),
      radial-gradient(ellipse 16% 38% at 52% 55%, var(--map-shade), rgba(38, 86, 156, 0) 100%),
      radial-gradient(ellipse 30% 28% at 70% 30%, var(--map-shade), rgba(38, 86, 156, 0) 100%),
      radial-gradient(ellipse 10% 12% at 85% 78%, var(--map-shade), rgba(38, 86, 156, 0) 100%);
  }
  .card--back .wordmark { left: 111px; top: 140px; gap: 24px; }
  .card--back .wordmark__square { background: var(--paper-white); width: 56px; height: 56px; }
  .card--back .wordmark__name { color: var(--paper-white); font-size: 58px; letter-spacing: 2px; gap: 6px; }
</style>
</head>
<body>
<main class="canvas">

  <section class="card card--front" aria-label="Business card front">
    <div class="pattern-zone" role="img" aria-label="Large faint pale blue brand pattern"></div>

    <div class="wordmark">
      <span class="wordmark__square"></span>
      <span class="wordmark__name"><span>Keystone</span><span>Spine</span></span>
    </div>

    <div class="holder">
      <div class="holder__name">Marcus Hale</div>
      <div class="holder__role">President</div>
    </div>

    <ul class="contact-list">
      <li>
        <svg viewBox="0 0 20 20"><path d="M6 1h8a1.5 1.5 0 0 1 1.5 1.5v15A1.5 1.5 0 0 1 14 19H6a1.5 1.5 0 0 1-1.5-1.5v-15A1.5 1.5 0 0 1 6 1zm0 2v12h8V3zm4 13a1 1 0 1 0 0 2 1 1 0 0 0 0-2z"/></svg>
        012 3456 7890
      </li>
      <li>
        <svg viewBox="0 0 20 20"><path d="M1 7c2-3 16-3 18 0v2h-4V7.5c-2-.7-8-.7-10 0V9H1zM4 10h12l2 7H2zm6 1.5a2.5 2.5 0 1 0 0 5 2.5 2.5 0 0 0 0-5z"/></svg>
        012 3456 7890
      </li>
      <li>
        <svg viewBox="0 0 20 20"><path d="M1 4h16v7h-1.5V6.2L9 11 2.5 6.2V14H11v1.5H1zm2.5 0L9 8.5 14.5 4zM15.5 12a3.5 3.5 0 1 1 0 7 3.5 3.5 0 0 1 0-7zm-1.8 3.4-.7.7 1.8 1.8 2.6-2.9-.7-.6-1.9 2.1z"/></svg>
        info@yourmail.com
      </li>
      <li>
        <svg viewBox="0 0 20 20"><path d="M10 1a9 9 0 1 1 0 18 9 9 0 0 1 0-18zm-1 2.1A7 7 0 0 0 3.1 9H6c.1-2.3.8-4.4 3-5.9zm2 0c2.2 1.5 2.9 3.6 3 5.9h2.9A7 7 0 0 0 11 3.1zM8 9h4c-.1-2-.7-3.8-2-5-1.3 1.2-1.9 3-2 5zm-4.9 2A7 7 0 0 0 9 16.9c-2.2-1.5-2.9-3.6-3-5.9zm4.9 0c.1 2 .7 3.8 2 5 1.3-1.2 1.9-3 2-5zm6 0c-.1 2.3-.8 4.4-3 5.9a7 7 0 0 0 5.9-5.9z"/></svg>
        www.yourwebside.com
      </li>
    </ul>

    <div class="address">
      <svg viewBox="0 0 18 26"><path d="M9 0a9 9 0 0 1 9 9c0 6-9 17-9 17S0 15 0 9a9 9 0 0 1 9-9zm0 5.5a3.5 3.5 0 1 0 0 7 3.5 3.5 0 0 0 0-7z"/></svg>
      012 Physical Address 000<br>
      NWYX, United State 5551
    </div>
  </section>

  <section class="card card--back" aria-label="Business card back">
    <div class="world-map" role="img" aria-label="Faint world map in a slightly darker blue"></div>
    <div class="wordmark">
      <span class="wordmark__square"></span>
      <span class="wordmark__name"><span>Keystone</span><span>Spine</span></span>
    </div>
  </section>

</main>
</body>
</html>
```